Life Coach for Lawyers Business Card Design

Elegant, original, business card design for life coaching service for associate attorneys who work in big law and struggle with stress, overwhelm, and time management. Double sided design.

Target Market(s)

Women associate attorneys who work in big law and struggle with stress, overwhelm, and time management.

Industry/Entity Type

Life Coaching

Contact Information for Business Card

Marissa Pendrell
Life Coach
518.677.3941
calmbriefcounsel.net
marissa@calmbriefcounsel.net
@calmbriefcounsel (Instagram)

Font styles to use
Other font styles liked:
• Silver South font duo. See uploaded files.

Requirements
Must have
• Icons for phone, website, email, and Instagram instead of words. Specific colors used in my logo (171B2B, 421121, FFFFFF)
Nice to have
• Foil. Embossed. Feminine design.
Should not have
• Any colors other than those used in logo. See uploaded files.

```html
<!DOCTYPE html>
<html lang="en">
<head>
<meta charset="utf-8">
<title>Calm Brief Counsel – Business Card</title>
<link rel="stylesheet" href="https://fonts.googleapis.com/css2?family=Poppins:wght@400;600;700&family=Playfair+Display:wght@400&display=swap">
<style>
  :root {
    --navy: #171B2B;
    --wine: #421121;
    --white: #FFFFFF;
    --backdrop: #E9E9EB;
  }
  * { box-sizing: border-box; margin: 0; padding: 0; }
  html, body { width: 1200px; height: 1200px; overflow: hidden; }
  body {
    background: var(--backdrop);
    font-family: "Poppins", sans-serif;
    color: var(--navy);
    position: relative;
  }
  .card {
    position: absolute;
    left: 250px;
    width: 700px;
    height: 400px;
    border-radius: 4px;
    box-shadow: 0 10px 30px rgba(23, 27, 43, 0.18);
    overflow: hidden;
  }
  /* Contact side */
  .card-front { top: 120px; background: var(--white); }
  .identity {
    position: absolute;
    top: 56px;
    right: 60px;
    display: flex;
    align-items: center;
    gap: 12px;
  }
  .identity-icon { width: 36px; height: 36px; }
  .identity-text { text-align: right; }
  .identity-name {
    font-weight: 700;
    font-size: 27px;
    letter-spacing: 0.5px;
    text-transform: uppercase;
    line-height: 1;
  }
  .identity-role {
    font-weight: 600;
    font-size: 11px;
    letter-spacing: 1px;
    text-transform: uppercase;
    margin-top: 4px;
  }
  .contact-band {
    position: absolute;
    left: 0;
    top: 196px;
    width: 350px;
    height: 14px;
    background: var(--navy);
  }
  .contact-label {
    position: absolute;
    left: 214px;
    top: 172px;
    height: 34px;
    padding: 0 18px;
    background: var(--navy);
    color: var(--white);
    font-weight: 600;
    font-size: 17px;
    line-height: 34px;
    text-transform: uppercase;
    letter-spacing: 0.5px;
  }
  .contact-list {
    position: absolute;
    left: 70px;
    top: 232px;
    list-style: none;
  }
  .contact-item {
    display: flex;
    align-items: center;
    gap: 16px;
    height: 38px;
    font-size: 16px;
  }
  .contact-icon {
    width: 30px;
    height: 30px;
    flex: none;
  }
  .contact-at {
    width: 30px;
    height: 30px;
    border: 2.5px solid var(--navy);
    border-radius: 6px;
    display: flex;
    align-items: center;
    justify-content: center;
    font-weight: 600;
    font-size: 16px;
    line-height: 1;
    flex: none;
  }
  /* Brand side */
  .card-back { top: 660px; background: var(--navy); }
  .brand-frame {
    position: absolute;
    inset: 60px 70px;
    border: 3px solid var(--white);
    display: flex;
    align-items: center;
    justify-content: center;
  }
  .brand-name {
    font-family: "Playfair Display", serif;
    font-weight: 400;
    color: var(--white);
    font-size: 50px;
    letter-spacing: 4px;
    text-transform: uppercase;
    text-align: center;
    line-height: 1.1;
  }
</style>
</head>
<body>

<section class="card card-front">
  <div class="identity">
    <svg class="identity-icon" viewBox="0 0 36 36" aria-hidden="true">
      <rect width="36" height="36" rx="7" fill="var(--navy)"/>
      <circle cx="18" cy="13" r="6" fill="var(--white)"/>
      <path d="M7 30c1-7 6-10 11-10s10 3 11 10z" fill="var(--white)"/>
    </svg>
    <div class="identity-text">
      <p class="identity-name">Marissa Pendrell</p>
      <p class="identity-role">Life Coach</p>
    </div>
  </div>

  <div class="contact-band"></div>
  <div class="contact-label">Contact Us</div>

  <ul class="contact-list">
    <li class="contact-item">
      <svg class="contact-icon" viewBox="0 0 30 30" aria-label="Phone">
        <rect width="30" height="30" rx="6" fill="var(--navy)"/>
        <path d="M10 7l3 4-2 2c1 3 3 5 6 6l2-2 4 3-2 3c-7 0-13-6-13-13z" fill="var(--white)"/>
      </svg>
      <span>518.677.3941</span>
    </li>
    <li class="contact-item">
      <svg class="contact-icon" viewBox="0 0 30 30" aria-label="Email">
        <rect x="1.5" y="1.5" width="27" height="27" rx="5" fill="none" stroke="var(--navy)" stroke-width="2.5"/>
        <rect x="6" y="9" width="18" height="12" fill="none" stroke="var(--navy)" stroke-width="2"/>
        <path d="M6 9l9 7 9-7M6 21l7-6M24 21l-7-6" fill="none" stroke="var(--navy)" stroke-width="2"/>
      </svg>
      <span>marissa@calmbriefcounsel.net</span>
    </li>
    <li class="contact-item">
      <span class="contact-at" aria-label="Instagram">@</span>
      <span>@calmbriefcounsel</span>
    </li>
    <li class="contact-item">
      <svg class="contact-icon" viewBox="0 0 30 30" aria-label="Website">
        <rect x="1.5" y="1.5" width="27" height="27" rx="5" fill="none" stroke="var(--navy)" stroke-width="2.5"/>
        <rect x="7" y="8" width="16" height="11" fill="var(--navy)"/>
        <rect x="5" y="20" width="20" height="2.5" fill="var(--navy)"/>
      </svg>
      <span>calmbriefcounsel.net</span>
    </li>
  </ul>
</section>

<section class="card card-back">
  <div class="brand-frame">
    <p class="brand-name">Calm Brief<br>Counsel</p>
  </div>
</section>

</body>
</html>
```